KELO Logistics App for American company. Will be like Zimo freight but more grassroots

We need a logistics App, similar to a truck broker. Similar to the Zimo or Pask apps where a truck driver can connect with companies and pick up the freight to get paid. The company is called KELO after the Morroxan explorer Sahl Qoremmi. Zimo freight has an app can be similar but more driver focused.

Target Market(s)

Everyone who needs freight moved from one place to next

Industry/Entity Type

Trucking

Requirements
Must have
• GPS and easy to use interface between driver and companies
Nice to have
• Colors that are travel like and friendly
Should not have
• Be boring or plain or hard to understand

```html
<!DOCTYPE html>
<html lang="en">
<head>
<meta charset="utf-8">
<title>Kelo Logistics – App Screens</title>
<link rel="stylesheet" href="https://fonts.googleapis.com/css2?family=Poppins:wght@400;500;600;700&display=swap">
<style>
  :root{
    --blue:#1a22f0;
    --blue-soft:#3f4bf4;
    --blue-pale:#6b74f7;
    --ink:#222;
    --muted:#8a8a8a;
    --line:#e4e4e4;
    --panel-grey:#f1f1f1;
    --white:#fff;
    --canvas:#fff;
  }
  *{box-sizing:border-box;margin:0;padding:0}
  html,body{width:1200px;height:848px;overflow:hidden;background:var(--canvas)}
  body{font-family:"Poppins",sans-serif;color:var(--ink);position:relative}
  .screen{position:absolute;top:31px;width:356px;height:772px;overflow:hidden;box-shadow:0 0 6px rgba(0,0,0,.18)}
  .screen--welcome{left:30px}
  .screen--board{left:419px;background:var(--blue)}
  .screen--details{left:806px;background:#f7f7f7}

  /* welcome */
  .welcome__photo{position:absolute;inset:0;background:linear-gradient(180deg,#8a8f96 0%,#a89a8c 30%,#8d8e92 55%,#6d7481 80%,#4a4f5c 100%)}
  .welcome__title{position:absolute;top:14px;left:0;right:0;text-align:center;color:var(--white);font-weight:600;font-size:25px}
  .welcome__text{position:absolute;top:58px;left:28px;right:28px;text-align:center;color:var(--white);font-size:14.5px;line-height:28px}

  /* shared headings */
  .screen__title{position:absolute;left:0;right:0;text-align:center;color:var(--white);font-weight:600;font-size:26px}
  .screen__sub{position:absolute;left:0;right:0;text-align:center;color:var(--white);font-size:17px;line-height:29px}

  /* loadboard */
  .board__wave{position:absolute;inset:0}
  .board .screen__title{top:16px}
  .board .screen__sub{top:64px}
  .card{position:absolute;left:12px;top:138px;width:333px;height:541px;background:var(--white);border-radius:3px;overflow:hidden}
  .card__head{height:50px;border-bottom:1px solid var(--line);display:flex;align-items:center;justify-content:space-between;padding:0 9px}
  .card__head h2{font-weight:400;font-size:21px}
  .icon-dot{width:28px;height:28px;border-radius:50%;background:var(--blue);display:flex;align-items:center;justify-content:center}
  .week{position:absolute;top:58px;left:0;width:333px;display:flex;justify-content:space-between;padding:0 10px 0 9px}
  .week__day{width:30px;text-align:center;font-size:16px}
  .week__day span{display:block;margin-top:8px;color:#b5b5b5;font-size:17px;height:30px;line-height:30px}
  .week__day--active span{background:var(--blue);color:var(--white);border-radius:50%}
  .week-rule{position:absolute;top:135px;left:0;right:0;border-top:1px solid var(--line)}
  .search{position:absolute;top:151px;left:28px;width:276px;height:50px;border-radius:4px;box-shadow:0 1px 5px rgba(0,0,0,.2);display:flex;align-items:center;justify-content:space-between;padding:0 14px 0 12px;font-size:15px}
  .search__hint{color:#aaa}
  .sortbar{position:absolute;top:218px;left:0;right:0;text-align:center;font-size:15px}
  .sortbar__link{color:var(--blue);margin-left:10px}
  .list-rule{position:absolute;top:255px;left:0;right:0;border-top:1px solid var(--line)}
  .price{color:var(--blue);font-weight:600;font-size:17px}
  .meta{color:var(--muted);font-size:12.5px}
  .meta span+span{margin-left:14px}
  .load__price{position:absolute;top:276px;left:15px}
  .load__note{position:absolute;top:270px;left:184px;width:140px;color:#555;font-size:12.5px;line-height:21px}
  .load__meta{position:absolute;top:311px;left:15px}
  .route{position:absolute;left:20px;top:346px}
  .route__line{position:absolute;left:6px;top:16px;height:58px;border-left:1px dashed #333}
  .stop{position:relative;padding-left:33px;margin-bottom:18px}
  .stop::before{content:"";position:absolute;left:0;top:11px;width:13px;height:13px;border-radius:50%;background:#111}
  .stop__city{font-size:14px}
  .stop__date{font-size:12px;color:#666}
  .load__foot{position:absolute;left:0;right:0;top:457px;height:84px;background:var(--panel-grey);padding:12px 14px}
  .load__foot h3{font-weight:400;font-size:14.5px}
  .load__foot p{margin-top:6px;width:190px;color:#666;font-size:12.5px;line-height:20px}
  .load__foot .price{position:absolute;right:20px;top:28px;font-weight:400;font-size:22px}

  /* nav */
  .nav{position:absolute;left:0;right:0;bottom:0;height:64px;display:flex;justify-content:space-around;align-items:center;padding:0 24px;color:var(--white);font-size:14px}
  .board .nav{background:var(--blue-soft)}
  .details .nav{background:var(--blue)}
  .nav__item{display:flex;flex-direction:column;align-items:center;gap:2px}

  /* details */
  .details__hero{position:absolute;left:0;right:0;top:0;height:190px;background:linear-gradient(120deg,#1a22f0 0%,#2f3bf2 55%,#5a64f0 80%,#3a45ee 100%)}
  .details .screen__title{top:36px}
  .details .screen__sub{top:78px;font-size:24px}
  .panel{position:absolute;left:0;right:0;top:166px;bottom:0;background:linear-gradient(180deg,#fff 0%,#f3f3f3 100%);border-radius:26px 26px 0 0}
  .panel__bar{position:absolute;top:18px;left:24px;right:24px;display:flex;justify-content:space-between;align-items:center}
  .panel__bar h2{color:var(--blue);font-weight:500;font-size:15px}
  .map{position:absolute;top:54px;left:12px;width:333px;height:219px;background:linear-gradient(135deg,#e6e7ea 0%,#dcdfe3 50%,#e9e7e2 100%);box-shadow:0 1px 5px rgba(0,0,0,.2)}
  .details .price{position:absolute;top:304px;left:27px}
  .details .meta{position:absolute;top:330px;left:27px}
  .pickup{position:absolute;top:366px;left:34px;padding-left:29px}
  .pickup::before{content:"";position:absolute;left:0;top:10px;width:12px;height:12px;border-radius:50%;background:#111}
  .pickup::after{content:"";position:absolute;left:5px;top:22px;height:60px;border-left:1px dashed #333}
  .pickup h3{color:var(--blue);font-weight:500;font-size:18px;line-height:24px}
  .pickup__city{margin-top:4px;font-size:14px}
  .pickup__date{font-size:12.5px;color:#666}
  .pickup__rating{font-size:10px;color:#666;letter-spacing:.3px}
  .pickup__rating b{color:#777;letter-spacing:-1px;font-weight:400}
  .chevron{position:absolute;top:387px;right:32px}
  .btn-book{position:absolute;top:466px;left:92px;width:173px;height:51px;border:1px solid var(--blue);border-radius:3px;background:transparent;color:var(--blue);font:400 16px "Poppins",sans-serif;text-decoration:underline;text-underline-offset:3px}
</style>
</head>
<body>

<section class="screen screen--welcome">
  <div class="welcome__photo" role="img" aria-label="Photo of a smiling warehouse manager in a grey shirt standing beside stacked shelves"></div>
  <h1 class="welcome__title">Kelo Logistics</h1>
  <p class="welcome__text">Lorem ipsum dolor sit amet, consectet ur adipiscing elit, sed do eiusmod tempor incididunt ut</p>
</section>

<section class="screen screen--board board">
  <svg class="board__wave" width="356" height="772" viewBox="0 0 356 772">
    <path d="M180 0 H356 V772 H245 C210 720 200 690 230 660 L300 600 L356 0 Z" fill="none"/>
    <path d="M180 0 C260 30 300 80 330 150 L356 150 V0 Z" fill="var(--blue-soft)"/>
    <path d="M190 720 C215 740 225 755 232 772 H0 V708 H180 Z" fill="var(--blue-soft)"/>
  </svg>
  <h1 class="screen__title">Kelo Logistics</h1>
  <p class="screen__sub">Easily Search Our Exclusive<br>Loadboard</p>

  <div class="card">
    <div class="card__head">
      <span class="icon-dot"><svg width="14" height="14" viewBox="0 0 14 14" fill="none" stroke="#fff" stroke-width="1.6"><rect x="1.5" y="2.5" width="11" height="10" rx="1.5"/><path d="M4 1v3M10 1v3M1.5 5.5h11"/><circle cx="7" cy="9" r="1.6"/></svg></span>
      <h2>Book</h2>
      <span class="icon-dot"><svg width="14" height="13" viewBox="0 0 14 13"><path d="M7 12.5 1.3 6.8A3.3 3.3 0 0 1 7 2.3a3.3 3.3 0 0 1 5.7 4.5Z" fill="#fff"/></svg></span>
    </div>
    <div class="week">
      <div class="week__day week__day--active">M<span>1</span></div>
      <div class="week__day">T<span>2</span></div>
      <div class="week__day">W<span>3</span></div>
      <div class="week__day">T<span>4</span></div>
      <div class="week__day">F<span>5</span></div>
      <div class="week__day">S<span>6</span></div>
      <div class="week__day">S<span>7</span></div>
    </div>
    <div class="week-rule"></div>
    <div class="search">
      <span><span class="search__hint">All Loads</span> Near you</span>
      <svg width="15" height="15" viewBox="0 0 15 15" fill="none" stroke="#555" stroke-width="2"><circle cx="6" cy="6" r="4.5"/><path d="m9.5 9.5 4 4"/></svg>
    </div>
    <p class="sortbar">Today <span class="sortbar__link">Sort - Deadhead</span></p>
    <div class="list-rule"></div>

    <p class="price load__price">$450</p>
    <p class="load__note">Lorem ipsum dolor sit amet, consectetur</p>
    <p class="meta load__meta"><span>5ml</span><span>Deadhead</span></p>
    <div class="route">
      <div class="route__line"></div>
      <div class="stop"><p class="stop__city">Houston, Tx</p><p class="stop__date">05-11-2021</p></div>
      <div class="stop"><p class="stop__city">Houston, Tx</p><p class="stop__date">05-11-2021</p></div>
    </div>
    <div class="load__foot">
      <h3>Lorem ipsum dolor sit amet</h3>
      <p>Lorem ipsum dolor sit amet, consectetur adipiscing</p>
      <span class="price">$400</span>
    </div>
  </div>

  <nav class="nav">
    <div class="nav__item"><svg width="18" height="18" viewBox="0 0 18 18" fill="none" stroke="#fff" stroke-width="2.4"><circle cx="7.5" cy="7.5" r="5.5"/><path d="m11.5 11.5 5 5"/></svg>Book</div>
    <div class="nav__item"><svg width="16" height="19" viewBox="0 0 16 19" fill="none" stroke="#fff" stroke-width="1.8"><path d="M2 1.5h12v16l-6-4.5-6 4.5Z"/></svg>My Loads</div>
    <div class="nav__item"><svg width="16" height="19" viewBox="0 0 16 19" fill="#fff"><circle cx="8" cy="4" r="3.5"/><path d="M3 9h10l1 6H2Z"/><rect x="1" y="16" width="14" height="2.5" rx="1"/></svg>Drivers</div>
    <div class="nav__item"><svg width="18" height="19" viewBox="0 0 18 19" fill="none" stroke="#fff" stroke-width="1.8"><circle cx="9" cy="5" r="4"/><path d="M1.5 18v-2a4 4 0 0 1 4-4h7a4 4 0 0 1 4 4v2Z"/></svg>Acccount</div>
  </nav>
</section>

<section class="screen screen--details details">
  <div class="details__hero" role="img" aria-label="Faded photo of a freight truck on the highway in blue tones"></div>
  <h1 class="screen__title">Kelo Logistics</h1>
  <p class="screen__sub">View Full Load Deatils</p>

  <div class="panel">
    <div class="panel__bar">
      <svg width="16" height="10" viewBox="0 0 16 10" fill="none" stroke="#333" stroke-width="1.6"><path d="M16 5H2M6 1 2 5l4 4"/></svg>
      <h2>Load Details</h2>
      <svg width="10" height="16" viewBox="0 0 10 16"><circle cx="5" cy="5" r="4" fill="#555"/><path d="M5 8v8" stroke="#555" stroke-width="1.6"/></svg>
    </div>
    <div class="map" role="img" aria-label="Street map of the city with three pickup markers and a current location dot"></div>

    <p class="price">$450</p>
    <p class="meta"><span>5ml</span><span>Deadhead</span></p>
    <div class="pickup">
      <h3>Pick Up</h3>
      <p class="pickup__city">Houston, Tx</p>
      <p class="pickup__date">05-11-2021</p>
      <p class="pickup__rating"><b>★★★★★</b> 4.9</p>
    </div>
    <svg class="chevron" width="10" height="18" viewBox="0 0 10 18" fill="none" stroke="#999" stroke-width="1.6"><path d="m1 1 8 8-8 8"/></svg>
    <button class="btn-book">BOOK LOAD</button>
  </div>

  <nav class="nav">
    <div class="nav__item"><svg width="18" height="18" viewBox="0 0 18 18" fill="none" stroke="#fff" stroke-width="2.4"><circle cx="7.5" cy="7.5" r="5.5"/><path d="m11.5 11.5 5 5"/></svg>Book</div>
    <div class="nav__item"><svg width="16" height="19" viewBox="0 0 16 19" fill="none" stroke="#fff" stroke-width="1.8"><path d="M2 1.5h12v16l-6-4.5-6 4.5Z"/></svg>My Loads</div>
    <div class="nav__item"><svg width="16" height="19" viewBox="0 0 16 19" fill="#fff"><circle cx="8" cy="4" r="3.5"/><path d="M3 9h10l1 6H2Z"/><rect x="1" y="16" width="14" height="2.5" rx="1"/></svg>Drivers</div>
    <div class="nav__item"><svg width="18" height="19" viewBox="0 0 18 19" fill="none" stroke="#fff" stroke-width="1.8"><circle cx="9" cy="5" r="4"/><path d="M1.5 18v-2a4 4 0 0 1 4-4h7a4 4 0 0 1 4 4v2Z"/></svg>Acccount</div>
  </nav>
</section>

</body>
</html>
```